Sydney law firm, Pelbury Solicitors, needs a flyer design!

We need a flyer design for our law firm which has been operating in Sydney for over 35 years. We want to send the flyer out to potential clients and also to existing clients to let them know the range of services that we provide. Our corporate colours are white, red and black and we would like these incorporated somewhat. The final design should be clean, modern and professional.

We would like the design to fit a double sided flyer approx. 210mm high x 100mm wide.

Law Firm

Serif
Sans Serif

eb2026
ffffff

• Details needed on the flyer are:
• Pelbury Solicitors
• 3/82 Tarrow Street, Liverpool, NSW 2170
• (02) 9413 5862
• www.pelburysolicitors-example.com.au
• info@pelburysolicitors-example.com.au
• Our areas of practice include:
• Property Law
• Conveyancing
• Leases
• Criminal Law
• Family Law
• Litigation and Dispute Resolution
• Company Law
• Wills and Estates
• Powers of Attorney and Guardianship
• a picture of scales or a picture of a gavel

```html
<!DOCTYPE html>
<html lang="en">
<head>
<meta charset="utf-8">
<title>Pelbury Solicitors Flyer Design_02</title>
<link rel="stylesheet" href="https://fonts.googleapis.com/css2?family=Arimo:wght@400;700&family=Crimson+Text:wght@400&display=swap">
<style>
  :root {
    --brand-red: #eb2026;
    --ink: #111111;
    --body-text: #333333;
    --paper: #ffffff;
    --board: #ffffff;
    --panel-edge: #c9c9c9;
    --rule: #e7a3a6;
    --photo-light: #cdb79c;
    --photo-mid: #8a7a68;
    --photo-dark: #2a2c33;
  }
  * { box-sizing: border-box; margin: 0; padding: 0; }
  html, body { width: 1200px; height: 1000px; overflow: hidden; background: var(--board); }
  .board { position: relative; width: 1200px; height: 1000px; font-family: "Arimo", Arial, sans-serif; }
  .board-title, .view-label {
    position: absolute; font-family: "Crimson Text", Georgia, serif; color: var(--ink);
    text-align: center;
  }
  .board-title { top: 64px; left: 0; width: 1200px; font-size: 21px; }
  .view-label { top: 908px; width: 382px; font-size: 20px; }
  .view-label.front { left: 194px; }
  .view-label.reverse { left: 624px; }

  .flyer {
    position: absolute; top: 110px; width: 382px; height: 780px;
    background: var(--paper); border: 1px solid var(--panel-edge);
    box-shadow: 3px 3px 4px rgba(0,0,0,0.25);
  }
  .flyer.front { left: 194px; }
  .flyer.reverse { left: 624px; }

  .brand {
    position: absolute; top: 42px; right: 46px;
    font-family: "Arimo", Arial, sans-serif; font-weight: 400;
    font-size: 15px; letter-spacing: 1px; color: var(--ink);
    text-transform: uppercase;
  }
  .header-rule { position: absolute; top: 100px; left: 0; width: 100%; height: 1px; background: var(--rule); }

  .hero-photo {
    position: absolute; top: 101px; left: 0; width: 100%; height: 252px;
    background: linear-gradient(100deg, var(--photo-light) 0%, var(--photo-mid) 45%, var(--photo-dark) 75%, var(--photo-mid) 100%);
  }

  .content { position: absolute; left: 46px; width: 300px; color: var(--body-text); font-size: 11.3px; line-height: 15.2px; }
  .headline { position: absolute; top: 386px; left: 46px; font-size: 29px; line-height: 34px; font-weight: 700; color: var(--ink); }
  .front .intro { top: 461px; }
  .content p + p { margin-top: 10px; }

  .reverse .intro { top: 134px; }
  .practice-list { list-style: none; margin-top: 10px; }
  .practice-list li { position: relative; padding-left: 14px; line-height: 19px; }
  .practice-list li::before {
    content: ""; position: absolute; left: 0; top: 6px; width: 7px; height: 7px;
    border: 1px solid var(--brand-red);
  }

  .contact { top: 608px; }
  .contact-heading { font-weight: 700; color: var(--ink); margin-bottom: 10px; }
  .contact b { color: var(--ink); margin-right: 4px; }
  .contact .web { margin-top: 10px; color: var(--brand-red); font-weight: 700; }
</style>
</head>
<body>
<div class="board">
  <h1 class="board-title">Pelbury Solicitors Flyer Design_02</h1>

  <section class="flyer front">
    <div class="brand">Pelbury Solicitors</div>
    <div class="hero-photo" role="img" aria-label="Photograph of a team of solicitors in business suits standing in an office"></div>
    <h2 class="headline">Your Business is<br>Our Business</h2>
    <div class="content intro">
      <p>Pelbury Solicitors is a private law firm based<br>in Liverpool that has been servicing the Sydney area<br>for over 30 years. With a dedicated, professional<br>and friendly team we pride ourselves on delivering<br>an exceptional legal service to our clients.</p>
      <p>Offering a complete legal service at affordable rates,<br>our clients really do come first.</p>
    </div>
    <div class="content contact">
      <p class="contact-heading">For further information, please contact:</p>
      <p>Pelbury Solicitors<br>3/82 Tarrow Street<br>Liverpool, NSW 2170<br><b>T</b> 02 9413 5862<br><b>E</b> info@pelburysolicitors-example.com.au</p>
      <p class="web">www.pelburysolicitors-example.com.au</p>
    </div>
  </section>

  <section class="flyer reverse">
    <div class="brand">Pelbury Solicitors</div>
    <div class="header-rule"></div>
    <div class="content intro">
      <p>Clients benefit from our extensive knowledge of the law,<br>vast network of professional and legal advisers as well as<br>our unmatched client service experience. We understand<br>the complex nature of the law and legal transactions<br>and strive to simplify the process for our clients. Through<br>communication, knowledge and focus we help our clients<br>understand where they want to be and how they can get<br>there. The law is constantly changing and with clients<br>ranging from individuals to large corporations we ensure<br>that our legal solutions are up-to-date and tailored to our<br>clients' individual needs.</p>
      <p>We are passionate about our profession and committed<br>to delivering results for our clients, so no matter what your<br>legal enquiry is we are happy to listen.</p>
      <p>Our areas of practice include:</p>
      <ul class="practice-list">
        <li>Property Law</li>
        <li>Conveyancing</li>
        <li>Leases</li>
        <li>Criminal Law</li>
        <li>Family Law</li>
        <li>Litigation and Dispute Resolution</li>
        <li>Company Law</li>
        <li>Wills and Estates</li>
        <li>Powers of Attorney and Guardianship</li>
      </ul>
    </div>
    <div class="content contact">
      <p class="contact-heading">For further information, please contact:</p>
      <p>Pelbury Solicitors<br>3/82 Tarrow Street<br>Liverpool, NSW 2170<br><b>T</b> 02 9413 5862<br><b>E</b> info@pelburysolicitors-example.com.au</p>
      <p class="web">www.pelburysolicitors-example.com.au</p>
    </div>
  </section>

  <p class="view-label front">Front view</p>
  <p class="view-label reverse">Reverse view</p>
</div>
</body>
</html>
```